Designer and consultant for professionals/businesses and manufacturers in the kitchen and bath in...

I have 30 years of design experience, and 19 of those years within the marketing team of a national cabinet manufacturer. This role gave me the opportunity to consult and design for kitchen/bath businesses, from boutique to multi-store national scale. My services include layout and spatial planning, individual display design, and product design for cabinet manufacturers. From showrooms, to trade shows to integrated design collections. I would like to see designs that convey professionalism, as well as an appeal to the creative designer mind!

Target Market(s)

Kitchen and bath dealers, as well as mid-scale multi-store home centers. Cabinet manufacturers, Trade Show agencies.

Industry/Entity Type

Kitchen

Contact Information for Business Card

Serving Kitchen and Bath Businesses

Logo Text

MT (initials for business name)

Font styles to use
Serif
Sans Serif
Decorative

Colors
e34197

Requirements
Must have
• Marlowe Tavish Design and Consulting, Inc. (business name)
• marlowe@mtvantra.com (email)
• 917-555-0148 (phone)
• mtvantra.com (website)
Nice to have
• Inclusions of geometric shapes; particularly a 30/15 degree triangle and circle(s)
• 2 colors
Should not have
• Not too artsy!

```html
<!DOCTYPE html>
<html lang="en">
<head>
<meta charset="utf-8">
<title>Marlowe Tavish Design and Consulting, Inc. — Business Card</title>
<link href="https://fonts.googleapis.com/css2?family=Nunito+Sans:wght@700&display=swap" rel="stylesheet">
<style>
  :root {
    --maroon: #5c0000;
    --copper: #d8844d;
    --paper: #ffffff;
    --page: #ffffff;
  }
  html, body {
    margin: 0;
    padding: 0;
    width: 1200px;
    height: 1000px;
    overflow: hidden;
    background: var(--page);
  }
  .business-card {
    position: absolute;
    left: 282px;
    top: 312px;
    width: 686px;
    height: 392px;
    background: var(--paper);
    overflow: hidden;
    font-family: "Nunito Sans", Arial, sans-serif;
  }
  .card-shapes {
    position: absolute;
    inset: 0;
    width: 686px;
    height: 392px;
  }
  .brand-name {
    position: absolute;
    left: 118px;
    top: 70px;
    width: 320px;
    text-align: center;
    color: var(--maroon);
    font-weight: 700;
    text-transform: uppercase;
    margin: 0;
  }
  .brand-name__primary {
    display: block;
    font-size: 30px;
    letter-spacing: 3px;
    line-height: 1.15;
  }
  .brand-name__secondary {
    display: block;
    font-size: 13px;
    letter-spacing: 2.5px;
    line-height: 1.6;
    margin-top: 6px;
  }
  .contact-list {
    position: absolute;
    right: 28px;
    top: 258px;
    margin: 0;
    padding: 0;
    list-style: none;
    text-align: right;
    color: var(--paper);
    font-size: 16px;
    font-weight: 700;
  }
  .contact-list li {
    height: 42px;
    line-height: 26px;
  }
</style>
</head>
<body>
  <article class="business-card">
    <svg class="card-shapes" viewBox="0 0 686 392" aria-hidden="true">
      <polygon class="band-top" points="408,0 686,0 686,156" fill="var(--copper)"/>
      <line class="rule-top" x1="313" y1="0" x2="686" y2="210" stroke="var(--maroon)" stroke-width="5"/>
      <line class="rule-bottom" x1="0" y1="166" x2="396" y2="392" stroke="var(--maroon)" stroke-width="5"/>
      <polygon class="band-bottom" points="0,220 300,392 0,392" fill="var(--copper)"/>
      <circle class="contact-disc" cx="563" cy="318" r="128" fill="var(--maroon)"/>
    </svg>

    <h1 class="brand-name">
      <span class="brand-name__primary">Marlowe Tavish</span>
      <span class="brand-name__secondary">Design &amp; Consulting Inc</span>
    </h1>

    <ul class="contact-list">
      <li class="contact-email">marlowe@mtvantra.com</li>
      <li class="contact-phone">917-555-0148</li>
      <li class="contact-web">mtvantra.com</li>
    </ul>
  </article>
</body>
</html>
```